We Need a GREAT Looking Sales Flyer!

Our small, boutique fitness facility needs a new flyer which highlights a new entry level fitness program that we are launching.

The flyer should be visually appealing as we will be handing a full color version to the potential member during our sales process.

I have attached:
- a word document which includes text
-Photos that can be used. Not all need to be used. These are to be used as you feel appropriate
- Our Logo

```html
<!DOCTYPE html>
<html lang="en">
<head>
<meta charset="utf-8">
<title>PulseForge – Change Begins Now</title>
<link rel="stylesheet" href="https://fonts.googleapis.com/css2?family=Alfa+Slab+One&family=Oswald:wght@400;600;700&family=Permanent+Marker&family=Rubik+Dirt&display=swap">
<style>
  :root {
    --stage: #6d6d6d;
    --cyan: #1fc3ee;
    --cyan-deep: #0f9cd0;
    --charcoal: #2b2b2e;
    --charcoal-deep: #1f1f21;
    --yellow: #f3e21a;
    --ink: #1c1c1e;
    --paper: #ffffff;
    --body-text: #dcdcdc;
    --photo-light: #d9d9d9;
    --photo-dark: #6a6a6a;
  }
  * { box-sizing: border-box; margin: 0; padding: 0; }
  html, body { width: 1113px; height: 1200px; overflow: hidden; }
  body { background: var(--stage); position: relative; }

  .flyer {
    position: absolute; left: 156px; top: 60px;
    width: 800px; height: 1080px; overflow: hidden;
    background: linear-gradient(160deg, var(--cyan) 0%, var(--cyan-deep) 60%);
    box-shadow: 0 12px 40px rgba(0,0,0,.35);
  }
  .flyer__backdrop { position: absolute; inset: 0; }

  .headline {
    position: absolute; white-space: nowrap;
    font-family: "Rubik Dirt", sans-serif; font-weight: 400;
    color: var(--paper); line-height: 1; text-shadow: 4px 4px 0 rgba(0,0,0,.35);
  }
  .headline--top { left: 215px; top: 50px; font-size: 118px; }
  .headline--bottom { left: 45px; top: 172px; font-size: 96px; }

  .hero-photo {
    position: absolute; left: 430px; top: 290px; width: 220px; height: 560px;
    background: linear-gradient(180deg, var(--photo-light), var(--photo-dark));
    border-radius: 6px;
  }

  .tagline {
    position: absolute; left: 30px; top: 340px; width: 380px;
    font-family: "Permanent Marker", sans-serif; font-weight: 400;
    font-size: 21px; line-height: 1.15; text-transform: uppercase;
    color: var(--yellow); text-align: center; transform: rotate(-10deg);
  }
  .program-name {
    position: absolute; left: 40px; top: 480px; white-space: nowrap;
    font-family: "Alfa Slab One", serif; font-weight: 400; font-size: 38px; line-height: 1.1;
    color: var(--ink); transform: rotate(-10deg);
  }

  .benefits { position: absolute; left: 80px; top: 700px; width: 330px; font-family: "Oswald", sans-serif; }
  .benefits__title {
    font-size: 42px; font-weight: 700; color: var(--yellow);
    border-bottom: 5px solid var(--yellow); padding-bottom: 4px; display: inline-block;
  }
  .benefits__list { list-style: none; margin-top: 14px; }
  .benefits__item { font-size: 16px; font-weight: 400; line-height: 1.2; color: var(--body-text); margin-bottom: 10px; }

  .bonus {
    position: absolute; left: 80px; bottom: 26px; width: 420px;
    border: 2px solid var(--yellow); border-radius: 12px; padding: 7px 14px;
    font-family: "Oswald", sans-serif; font-weight: 400; font-size: 16px; line-height: 1.2; color: var(--yellow);
  }

  .promise-badge {
    position: absolute; right: 22px; top: 730px; width: 112px; height: 112px;
    border: 3px solid var(--yellow); border-radius: 50%;
    display: flex; align-items: center; justify-content: center; text-align: center;
    font-family: "Oswald", sans-serif; font-weight: 600; font-size: 14px; line-height: 1.2;
    color: var(--yellow);
  }

  .offer {
    position: absolute; right: 50px; top: 862px; text-align: right;
    font-family: "Oswald", sans-serif; font-weight: 700; line-height: 1.15;
  }
  .offer__lead { font-size: 30px; color: var(--paper); }
  .offer__price { font-size: 36px; color: var(--yellow); }

  .brand {
    position: absolute; right: 50px; bottom: 36px;
    font-family: "Oswald", sans-serif; font-weight: 700; font-size: 34px; color: var(--paper);
  }
</style>
</head>
<body>
  <main class="flyer">
    <svg class="flyer__backdrop" width="800" height="1080" viewBox="0 0 800 1080" role="img" aria-label="Blue-tinted gym interior photo behind a diagonal yellow paint band and charcoal lower panel">
      <polygon points="0,660 800,380 800,1080 0,1080" fill="var(--charcoal)"/>
      <polygon points="0,620 800,340 800,400 0,690" fill="var(--yellow)"/>
      <polygon points="0,690 800,400 800,1080 0,1080" fill="var(--charcoal-deep)" opacity=".35"/>
    </svg>

    <h1>
      <span class="headline headline--top">CHANGE</span>
      <span class="headline headline--bottom">BEGINS NOW</span>
    </h1>

    <div class="hero-photo" role="img" aria-label="Black and white photo of a woman doing a dumbbell lunge"></div>

    <p class="tagline">The fitness program that is responsible for transforming over 924 lives!</p>
    <h2 class="program-name">THE ULTIMATE<br>KICK START</h2>

    <section class="benefits">
      <h3 class="benefits__title">WHAT YOU GET</h3>
      <ul class="benefits__list">
        <li class="benefits__item">Unlimited Group Training Designed Specifically<br>to Sculpt &amp; Tone the body.</li>
        <li class="benefits__item">CUSTOM Meal Plan designed specifically<br>for Your and Your Body Type</li>
        <li class="benefits__item">(2) Detailed Body Scans to track results</li>
        <li class="benefits__item">Supplement List to accelerate metabolism</li>
        <li class="benefits__item">10% off First Supplement Purchase to<br>Kickstart the process</li>
      </ul>
    </section>

    <p class="bonus">Exclusive access to PulseForge's Private Member Page for<br>additional recipes, Support and Guidance</p>

    <p class="promise-badge">The Life That<br>You Envision<br>IS POSSIBLE!</p>

    <div class="offer">
      <p class="offer__lead">GET STARTED FOR</p>
      <p class="offer__price">$199 (CROSSED OUT)</p>
      <p class="offer__price">ONLY $99 &nbsp;LIMITED TIME</p>
    </div>

    <p class="brand">PulseForge</p>
  </main>
</body>
</html>
```